Text only wordpress site to capture emails

Refer to inspiration upload for list of sites that will be useful for you.

We need a site that will be used to capture emails from clients that follow us on social media. The site will be all text, pretty simple. I have a couple of text sites that I like and we can use them for an example.

Menu section will have home, archive, about.
Footer will have © and Website Privacy Policy | Legal and Policies
There will be some text on the home page and an email capture.

This site will be all text no pictures.

I discuss Cubicle Chatter so the text portions will have some questions and answers on this and then prompt for the visitor to subscribe to my email list.

The only purpose of the site is to build an email list from existing social media followers so the site will be pretty simple in and of itself.

• Text only, similar Q&A to uploaded pics.

I will use a template from letter pinecone dotcom for email capture.

I like the simple couriernew font family that is on both sites supplied in the uploads.
• If you use any color it needs to be very minimal.

```html
<!DOCTYPE html>
<html lang="en">
<head>
<meta charset="utf-8">
<title>Cubicle Chatter</title>
<link href="https://fonts.googleapis.com/css2?family=Courier+Prime:wght@400;700&display=swap" rel="stylesheet">
<style>
  :root {
    --ink: #111111;
    --text: #333333;
    --muted: #8a8a8a;
    --rule: #cccccc;
    --field-border: #dddddd;
    --circle-border: #e3e3e3;
    --button: #cbcbcb;
    --paper: #ffffff;
  }
  * { box-sizing: border-box; margin: 0; padding: 0; }
  html, body {
    width: 1200px; height: 1185px; overflow: hidden;
    background: var(--paper); color: var(--text);
    font-family: "Courier Prime", "Courier New", monospace;
  }

  .site-header {
    height: 79px; border-bottom: 1px dashed var(--rule);
    display: flex; justify-content: space-between; align-items: flex-start;
    padding: 25px 168px 0 162px;
  }
  .site-title { font-size: 26px; line-height: 34px; font-weight: 700; color: var(--ink); letter-spacing: 1.6px; }
  .main-nav { display: flex; gap: 54px; margin-top: 10px; }
  .main-nav a { font-size: 13.5px; line-height: 18px; letter-spacing: 0.9px; color: var(--text); text-decoration: none; }

  .page { display: flex; padding: 47px 0 0 162px; height: 990px; overflow: hidden; }

  .newsletter { width: 268px; margin-right: 45px; }
  .newsletter h2 { font-size: 25px; line-height: 28px; font-weight: 700; color: var(--text); letter-spacing: 0.8px; margin-bottom: 11px; }
  .newsletter p { width: 262px; font-size: 11px; line-height: 18px; color: var(--muted); letter-spacing: 2.8px; margin-bottom: 17px; }
  .email-field {
    display: block; width: 265px; height: 37px; margin-left: -2px;
    border: 1px solid var(--field-border); border-radius: 3px;
    box-shadow: 0 2px 4px rgba(0,0,0,0.06);
    padding: 0 12px; font: 13px "Courier Prime", "Courier New", monospace; color: var(--muted);
    letter-spacing: 1px;
  }
  .subscribe-button {
    display: block; margin: 23px 0 0 -2px; width: 137px; height: 35px; border: 0; border-radius: 3px;
    background: var(--button); box-shadow: 0 2px 4px rgba(0,0,0,0.12);
    font: 700 13.5px "Courier Prime", "Courier New", monospace; color: var(--text);
    letter-spacing: 1px; padding-top: 3px;
  }

  .faq { width: 565px; }
  .faq h1 { font-size: 23px; line-height: 28px; font-weight: 700; color: var(--text); letter-spacing: 1px; margin-bottom: 11px; }
  .faq-intro { font-size: 12px; line-height: 18px; letter-spacing: 1px; margin-bottom: 37px; }
  .faq-item { margin-bottom: 35px; }
  .faq-question {
    display: flex; align-items: center; gap: 10px;
    font-size: 14px; line-height: 18px; font-weight: 700; color: var(--text);
    letter-spacing: 1.3px; margin-bottom: 11px;
  }
  .faq-question svg { flex: none; }
  .faq-answer { font-size: 12px; line-height: 22px; letter-spacing: 1px; }
  .faq-answer strong { color: var(--ink); }

  .site-footer {
    border-top: 1px dashed var(--rule); height: 116px;
    display: flex; justify-content: space-between; align-items: flex-start;
    padding: 33px 164px 0 162px; font-size: 12px; line-height: 18px; letter-spacing: 1.3px;
  }
  .legal-links { margin-top: 11px; }
  .legal-links a { color: var(--text); text-decoration: none; }
  .social { display: flex; align-items: center; gap: 10px; margin-top: 4px; }
  .social-label { margin-right: 4px; }
  .social-link {
    display: flex; align-items: center; gap: 6px;
    color: var(--text); text-decoration: none; font-size: 11px; letter-spacing: 1px;
  }
  .social-circle { width: 37px; height: 37px; border-radius: 50%; border: 1px solid var(--circle-border); }
</style>
</head>
<body>
  <header class="site-header">
    <div class="site-title">Cubicle Chatter</div>
    <nav class="main-nav">
      <a href="#">Home</a>
      <a href="#">Archive</a>
      <a href="#">About</a>
    </nav>
  </header>

  <main class="page">
    <aside class="newsletter">
      <h2>Newsletter</h2>
      <p>Lorem ipsum dolor sit ametere consectetuer adipiscing eoier eliter sederer diame nonummye nibh euismod tinci laor</p>
      <input class="email-field" type="email" placeholder="Email Here">
      <button class="subscribe-button">Subscribe</button>
    </aside>

    <section class="faq">
      <h1>What the...</h1>
      <p class="faq-intro">Lorem ipsum dolor sit amet consectetuer adipiscing elisederer</p>

      <article class="faq-item">
        <h3 class="faq-question"><svg width="12" height="10" viewBox="0 0 12 10"><path d="M1 1l4 4-4 4M6 1l4 4-4 4" fill="none" stroke="#333" stroke-width="1.2"/></svg>Sed diam nonummy</h3>
        <p class="faq-answer"><strong>A:</strong> Lorem ipsum dolor sit amet consectetuer adipiscing eliter sederer diame nonummy nibh euismod tincidunt ut laoreet dolore magna aliquam erat volutpat tincidunt ut laoreet dolore magna.</p>
      </article>
      <article class="faq-item">
        <h3 class="faq-question"><svg width="12" height="10" viewBox="0 0 12 10"><path d="M1 1l4 4-4 4M6 1l4 4-4 4" fill="none" stroke="#333" stroke-width="1.2"/></svg>Nibh euismod tincidun</h3>
        <p class="faq-answer"><strong>A:</strong> Lorem ipsum dolor sit amet consectetuer adipiscing eliter sederer diame nonummy nibh euismod tincidunt ut laoreet dolore magna aliquam erat volutpat tincidunt ut laoreet dolore magna.</p>
      </article>
      <article class="faq-item">
        <h3 class="faq-question"><svg width="12" height="10" viewBox="0 0 12 10"><path d="M1 1l4 4-4 4M6 1l4 4-4 4" fill="none" stroke="#333" stroke-width="1.2"/></svg>Lorem mpsum dolor</h3>
        <p class="faq-answer"><strong>A:</strong> Lorem ipsum dolor sit amet consectetuer adipiscing eliter sederer diame nonummy nibh euismod tincidunt ut laoreet.</p>
      </article>
      <article class="faq-item">
        <h3 class="faq-question"><svg width="12" height="10" viewBox="0 0 12 10"><path d="M1 1l4 4-4 4M6 1l4 4-4 4" fill="none" stroke="#333" stroke-width="1.2"/></svg>Nostrud exercitation</h3>
        <p class="faq-answer"><strong>A:</strong> Lorem ipsum dolor sit amet consectetuer adipiscing</p>
      </article>
      <article class="faq-item">
        <h3 class="faq-question"><svg width="12" height="10" viewBox="0 0 12 10"><path d="M1 1l4 4-4 4M6 1l4 4-4 4" fill="none" stroke="#333" stroke-width="1.2"/></svg>Duis autem veleum iriure</h3>
        <p class="faq-answer"><strong>A:</strong> Lorem ipsum dolor sit amet consectetuer adipiscing eliter sederer diame nonummy nibh euismod tincidunt ut laoreet dolore magna aliquam erat volutpat tincidunt ut laoreet dolore magna.</p>
      </article>
      <article class="faq-item">
        <h3 class="faq-question"><svg width="12" height="10" viewBox="0 0 12 10"><path d="M1 1l4 4-4 4M6 1l4 4-4 4" fill="none" stroke="#333" stroke-width="1.2"/></svg>Feugiat nulla facilisis</h3>
        <p class="faq-answer"><strong>A:</strong> Lorem ipsum dolor sit amet consectetuer adipiscing eliter sederer diame nonummy nibh euismod tincidunt ut laoreet dolore magna aliquam erat volutpat tincidunt ut laoreet dolore magna.</p>
      </article>
      <article class="faq-item">
        <h3 class="faq-question"><svg width="12" height="10" viewBox="0 0 12 10"><path d="M1 1l4 4-4 4M6 1l4 4-4 4" fill="none" stroke="#333" stroke-width="1.2"/></svg>Llandit praesent iuptatum deleni</h3>
        <p class="faq-answer"><strong>A:</strong> Lorem ipsum dolor sit amet consectetuer adipiscing eliter sederer diame nonummy nibh euismod tincidunt ut laoreet.</p>
      </article>
    </section>
  </main>

  <footer class="site-footer">
    <div class="footer-legal">
      <p>Copyright © 2021 Cubicle Chatter. All Rights Reserved.</p>
      <p class="legal-links"><a href="#">Privacy Policy</a> | <a href="#">Legal and Policies</a></p>
    </div>
    <div class="social">
      <span class="social-label">Follow Us:</span>
      <a class="social-link" href="#"><span class="social-circle"></span>Friendly</a>
      <a class="social-link" href="#"><span class="social-circle"></span>Chirper</a>
    </div>
  </footer>
</body>
</html>
```